Business Card Upgrade

I have designed our business card using our new logo. I think it needs imporovements. We used to have two cards for our business. One card was for our software business, and the other was for our consulting business. We are now in the process of combining our websites, marketing, name, and a new logo.

Our goal is to have a really sharp professional logo. One reason I designed the card the way I did was that our Titles are sometimes long, and by separating the person's name and title, it shows up very well and the title can be adjusted no matter how long it is. Sometimes the title can be 4 or 5 words or more.

We really like our logo on black as it shows up very nice. Our PMS colors are as follows: 368C and 459C.

The Designer that will be working with us will need to deliver the following:

The front and back of the Business Card Design will need to be delivered in a high quality JPEG, and
The front and back of the Business Card Design in Illustrator Format .ai
Any fonts will need to be sent to us if they are not standard and are required to open the Illustrator file correctly.

To help us get a good idea of the card with a title, please use the title: " Director of Software Development "

NOTE: The chosen designer will be selected to design our new letterhead within 2 weeks from the closing of this contest.

To help us make sure the card design works with longer titles, please use the followign job title on the card:  

"Director of Software and Product Development"

 

ALL DESIGNERS:

1. I appreciate the different angles you are showing the cards, but please be sure and always show the direct view, so I can see the layout and what the person I hand the card will see.

2. Please do not use white.  Please use off white as I don't care for white cards and they get dirty easy and do not represent the designs well.

Dear Designers,

Please provide samples straight one as a viewer of the card will see.  Some of the angles that are presented make it impossible to tell how everything fits, and sometimes even makes areas look skewed. So, please provide a straight sample view.

Pinnacle 400 company executives such as Vice Presidents, and Directors

Software

• Professional looking Card.

Our customers are Directors, Vice Presidents, and Presidents of companies as large as Pinnacle 400 companies. The card needs to get attention wile still looking professional.

Delivery of the finished product in Illustrator Format with any fonts needed to edit the text or open the file.

The card will be a heavy stock with a soft touch coating for that silk feel.

```html
<!DOCTYPE html>
<html lang="en">
<head>
<meta charset="utf-8">
<title>Tidewater Zone Partners – Business Card</title>
<link rel="stylesheet" href="https://fonts.googleapis.com/css2?family=Arimo:wght@400;700&display=swap">
<style>
  :root {
    --stage: #dcdcdc;
    --ink: #000000;
    --green: #5aaa0b;
    --cream: #e2d08c;
    --cream-text: #e6d592;
    --body-text: #111111;
  }
  * { margin: 0; padding: 0; box-sizing: border-box; }
  html, body { width: 1200px; height: 900px; overflow: hidden; }
  body {
    background: var(--stage);
    font-family: "Arimo", Arial, sans-serif;
    position: relative;
  }
  .card {
    position: absolute;
    width: 615px;
    height: 350px;
    overflow: hidden;
  }
  .card-front { left: 292px; top: 83px; background: var(--ink); }
  .card-back { left: 291px; top: 468px; background: var(--cream); }

  .front-brand {
    position: absolute;
    left: 0; right: 0; top: 150px;
    text-align: center;
    color: var(--green);
    font-weight: 700;
    font-size: 40px;
    letter-spacing: 1px;
  }
  .services {
    position: absolute;
    left: 0; right: 0; top: 256px;
    text-align: center;
    color: var(--green);
    font-size: 13px;
    letter-spacing: 0.3px;
  }
  .services .divider { color: var(--cream-text); font-weight: 700; margin: 0 3px; }
  .tagline {
    position: absolute;
    left: 0; right: 0; top: 277px;
    text-align: center;
    color: var(--cream-text);
    font-size: 9.5px;
    letter-spacing: 1px;
  }

  .person-name {
    position: absolute; left: 42px; top: 35px;
    font-weight: 700; font-size: 20px; color: var(--body-text);
  }
  .person-title {
    position: absolute; left: 42px; top: 57px;
    font-size: 14px; color: var(--green);
  }
  .address {
    position: absolute; left: 42px; top: 110px;
    font-size: 14px; line-height: 19.5px; color: var(--body-text); font-style: normal;
  }
  .address .company { color: var(--green); font-weight: 700; }
  .contact-line {
    position: absolute; left: 40px; top: 174px;
    display: flex; align-items: center; gap: 6px;
    font-size: 14px; color: var(--body-text);
  }
  .contact-line .icon { width: 17px; height: 17px; display: block; }
  .contact-line .email { margin-left: 6px; }

  .back-band { position: absolute; left: 0; top: 0; width: 615px; height: 350px; }
  .back-brand {
    position: absolute; right: 48px; top: 272px;
    color: var(--green); font-weight: 700; font-size: 21px;
  }
  .web {
    position: absolute; left: 40px; top: 315px;
    font-size: 14px; color: var(--cream-text);
  }
  .web strong { font-size: 17px; }
</style>
</head>
<body>

<section class="card card-front">
  <div class="front-brand">Tidewater Zone Partners</div>
  <p class="services">CONSULTING<span class="divider">|</span>SOFTWARE<span class="divider">|</span>OPERATIONS<span class="divider">|</span>ADMINISTRATION</p>
  <p class="tagline">THE ONLY FIRM WITH ENOUGH EXPERTISE TO OFFER EVERY FTZ SOLUTION</p>
</section>

<section class="card card-back">
  <svg class="back-band" viewBox="0 0 615 350" aria-hidden="true">
    <path d="M0 220 C 150 232, 260 250, 380 236 C 470 226, 540 220, 615 246 L615 350 L0 350 Z" fill="#5aaa0b"/>
    <path d="M0 230 C 150 252, 280 262, 400 248 C 480 240, 550 238, 615 250 L615 350 L0 350 Z" fill="#000000"/>
  </svg>

  <h1 class="person-name">DANA WHITFIELD</h1>
  <p class="person-title">Director of Software Development</p>

  <address class="address">
    <span class="company">Tidewater Zone Partners</span><br>
    418 Bayview Lane<br>
    Riverton, Ohio 45021
  </address>

  <div class="contact-line">
    <svg class="icon" viewBox="0 0 17 17" aria-hidden="true">
      <rect width="17" height="17" fill="#5aaa0b"/>
      <path d="M5 3.5 L7 3.5 L7.6 6 L6.4 7 C7 8.6 8.3 9.9 10 10.6 L11 9.4 L13.5 10 L13.5 12 C13.5 12.8 12.8 13.5 12 13.5 C7.9 13.3 3.7 9.1 3.5 5 C3.5 4.2 4.2 3.5 5 3.5 Z" fill="#111"/>
    </svg>
    <span>555.014.2780 (Direct)</span>
    <svg class="icon email" viewBox="0 0 17 17" aria-hidden="true">
      <rect width="17" height="17" fill="#5aaa0b"/>
      <rect x="3" y="5" width="11" height="7.5" fill="#e2d08c"/>
      <path d="M3 5 L8.5 9.3 L14 5" fill="none" stroke="#5aaa0b" stroke-width="1"/>
    </svg>
    <span>dwhitfield@tidewaterzp.com</span>
  </div>

  <div class="back-brand">Tidewater Zone Partners</div>
  <p class="web">www.<strong>tidewaterzp</strong>.com</p>
</section>

</body>
</html>
```